New National Dermatology Group needs a business card!

We need a business card for our new national company that has 3 brands within the business:
Brellow Clinics Australia, Tamvirk Clinics Australia and Orvandel Clinics Australia.
We help people access dermatology services close to home throughout Australia.
We need a business card that has:
all 3 logos on it,
Our websites (there are three, listed above)
Our email (there are three, listed above)
The location of our first clinic: 41 Wendle St Parramatta (this can then be changed for each location as required)

```html
<!DOCTYPE html>
<html lang="en">
<head>
<meta charset="utf-8">
<title>Business Card – Brellow, Tamvirk &amp; Orvandel Clinics Australia</title>
<link rel="stylesheet" href="https://fonts.googleapis.com/css2?family=Tinos:wght@400&display=swap">
<style>
  :root {
    --backdrop: #2b2b2b;
    --card-dark: #141414;
    --white: #ffffff;
    --orange: #ef8423;
    --green: #22ad4b;
    --brown: #8a4a1f;
    --olive: #6f7d30;
    --lime: #9db43a;
    --serif: "Tinos", "Times New Roman", serif;
  }
  * { margin: 0; padding: 0; box-sizing: border-box; }
  html, body { width: 1200px; height: 1108px; overflow: hidden; background: var(--backdrop); }
  .canvas {
    width: 1200px; height: 1108px;
    display: flex; justify-content: center; align-items: center; gap: 80px;
  }
  .card {
    width: 440px; height: 770px; border-radius: 18px;
    position: relative; overflow: hidden;
    display: flex; flex-direction: column; align-items: center; justify-content: center;
    font-family: var(--serif); text-align: center;
  }
  .card--front {
    color: var(--white);
    background:
      radial-gradient(circle at 100% 0%, var(--orange) 0%, rgba(239,132,35,0) 45%),
      radial-gradient(circle at 0% 0%, var(--lime) 0%, rgba(157,180,58,0) 40%),
      radial-gradient(circle at 0% 100%, var(--brown) 0%, rgba(138,74,31,0) 45%),
      radial-gradient(circle at 100% 100%, var(--olive) 0%, rgba(111,125,48,0) 45%),
      var(--green);
    gap: 26px;
  }
  .brand-block { display: flex; flex-direction: column; align-items: center; gap: 6px; }
  .brand-name {
    font-size: 25px; letter-spacing: 1px; text-transform: uppercase; line-height: 1.15;
    margin-bottom: 10px;
  }
  .contact-line { font-size: 17px; line-height: 1.3; }
  .divider { width: 30px; height: 1px; background: var(--white); }
  .card--back { background: var(--card-dark); gap: 80px; padding-bottom: 30px; }
  .card--back .brand-name { font-size: 30px; margin: 0; }
  .brand-name--tamvirk { color: var(--orange); }
  .brand-name--brellow { color: var(--green); }
  .brand-name--orvandel { color: var(--brown); }
  .colour-bar { position: absolute; left: 0; right: 0; bottom: 0; height: 24px; display: block; }
</style>
</head>
<body>
<main class="canvas">
  <section class="card card--front" aria-label="Card front with contact details">
    <div class="brand-block">
      <p class="brand-name">Tamvirk<br>Clinics Australia</p>
      <p class="contact-line">info@tamvirkclinicsaustralia.com</p>
      <p class="contact-line">tamvirkclinicsaustralia.com</p>
      <p class="contact-line">41 Wendle St Parramatta</p>
    </div>
    <span class="divider"></span>
    <div class="brand-block">
      <p class="brand-name">Brellow<br>Clinics Australia</p>
      <p class="contact-line">info@brellowclinicsaustralia.com</p>
      <p class="contact-line">brellowclinicsaustralia.com</p>
      <p class="contact-line">41 Wendle St Parramatta</p>
    </div>
    <span class="divider"></span>
    <div class="brand-block">
      <p class="brand-name">Orvandel<br>Clinics Australia</p>
      <p class="contact-line">info@orvandelclinicsaustralia.com</p>
      <p class="contact-line">orvandelclinicsaustralia.com</p>
      <p class="contact-line">41 Wendle St Parramatta</p>
    </div>
  </section>

  <section class="card card--back" aria-label="Card back with brand names">
    <p class="brand-name brand-name--tamvirk">Tamvirk<br>Clinics Australia</p>
    <p class="brand-name brand-name--brellow">Brellow<br>Clinics Australia</p>
    <p class="brand-name brand-name--orvandel">Orvandel<br>Clinics Australia</p>
    <svg class="colour-bar" viewBox="0 0 440 24" preserveAspectRatio="none" aria-hidden="true">
      <rect x="0" y="0" width="147" height="24" fill="#8a4a1f"/>
      <rect x="147" y="0" width="147" height="24" fill="#ef8423"/>
      <rect x="294" y="0" width="146" height="24" fill="#22ad4b"/>
    </svg>
  </section>
</main>
</body>
</html>
```